BrivoMatex. Lantern for the Steady Growth. Business card

Professional business card for BrivoMatex (Lantern for the Steady Growth)
My rationale: Strategy-> Execution-> Results-> Value that lead to the BrivoMatex name: We put the Lantern for the Steady Growth.
We deliver value to our customers helping them at defining a good strategy (cyan arrow). 90% of well formulated strategies fail due to poor execution so we also consider strategical execution very important (green arrow). Due to the execution we obtain the results (blue arrow). Finally, the results provide feedback to redefine strategy, and the new strategy has to be executed and new results obtained providing new feedback and on and on. It's like a wheel that finally, must create corporate value: value for shareholders, staholders, employees, providers...-

Target Market(s)

CEOs and steering comitees , invewrnent funds

Industry/Entity Type

Business Consultant

Contact Information for Business Card

Tommaso Ferlini
CEO & Founder
tommaso.ferlini@brivomatex.example
Mobile: +34 611.205.938
www.brivomatex.example

Colors

Designer to choose colors to be used in the design.

Requirements
Nice to have
• Nice to hace the words: Strategy, execution, results
• Nice to vave the claim: Lantern for the Steady Growth
• The three colors should be shown:
• cyan for STRATEGY
• green for EXECUTION
• blue for RESULTS
Should not have
• Complete black background

```html
<!DOCTYPE html>
<html lang="en">
<head>
<meta charset="utf-8">
<title>BrivoMatex Business Card</title>
<link href="https://fonts.googleapis.com/css2?family=Open+Sans:wght@400;600;700;800&display=swap" rel="stylesheet">
<style>
  :root {
    --royal: #233d9c;
    --royal-deep: #1c3188;
    --cyan: #29b3e6;
    --green: #a3cd3b;
    --white: #ffffff;
    --stage-light: #8a8a8a;
    --stage-dark: #4a4a4a;
  }
  * { margin: 0; padding: 0; box-sizing: border-box; }
  html, body { width: 1200px; height: 900px; overflow: hidden; }
  body {
    background: radial-gradient(ellipse at 50% 40%, var(--stage-light), var(--stage-dark));
    font-family: "Open Sans", Arial, sans-serif;
    position: relative;
  }
  .card {
    position: absolute;
    left: 300px;
    width: 600px;
    height: 343px;
    border-radius: 18px;
    overflow: hidden;
    box-shadow: 0 10px 24px rgba(0,0,0,0.35);
  }
  .card-front { top: 77px; background: var(--royal); }
  .card-back {
    top: 480px;
    background: linear-gradient(135deg, var(--royal) 0%, var(--royal-deep) 100%);
  }
  .front-bands { position: absolute; inset: 0; width: 100%; height: 100%; }

  .brand {
    position: absolute;
    display: flex;
    align-items: center;
    gap: 10px;
    font-weight: 800;
    letter-spacing: -0.5px;
  }
  .brand-dot { border-radius: 50%; flex: none; }
  .brand-front { left: 34px; top: 92px; font-size: 34px; color: var(--royal); }
  .brand-front .brand-dot { width: 22px; height: 22px; background: var(--cyan); }
  .brand-back { left: 50%; top: 50%; transform: translate(-50%, -60%); font-size: 44px; color: var(--white); }
  .brand-back .brand-dot { width: 28px; height: 28px; background: var(--white); }

  .identity { position: absolute; right: 30px; top: 100px; text-align: right; color: var(--white); }
  .person-name { font-size: 25px; font-weight: 700; line-height: 1.1; }
  .person-role { font-size: 17px; color: var(--cyan); margin-top: 2px; }
  .role-rule { display: block; width: 58px; height: 3px; background: var(--green); margin: 8px 0 0 auto; }

  .contacts { position: absolute; right: 24px; top: 198px; list-style: none; }
  .contact {
    display: flex; align-items: center; justify-content: flex-end;
    gap: 12px; height: 36px;
    color: var(--white); font-size: 14px;
  }
  .contact-icon {
    width: 26px; height: 26px; border-radius: 50%;
    background: var(--white);
    display: flex; align-items: center; justify-content: center;
  }
  .contact-icon svg { width: 14px; height: 14px; }

  .back-web {
    position: absolute; right: 30px; bottom: 24px;
    color: var(--white); font-size: 14px;
  }
</style>
</head>
<body>

  <section class="card card-front">
    <svg class="front-bands" viewBox="0 0 600 343" preserveAspectRatio="none" aria-hidden="true">
      <path d="M0,0 H345 C305,200 185,305 0,338 Z" fill="var(--green)"/>
      <path d="M0,0 H282 C270,190 170,308 0,330 Z" fill="var(--cyan)"/>
      <path d="M0,0 H245 C238,170 150,288 0,318 Z" fill="var(--white)"/>
    </svg>

    <div class="brand brand-front">
      <span class="brand-name">BrivoMatex</span>
      <span class="brand-dot"></span>
    </div>

    <div class="identity">
      <div class="person-name">Tommaso Ferlini</div>
      <div class="person-role">CEO &amp; Founder</div>
      <span class="role-rule"></span>
    </div>

    <ul class="contacts">
      <li class="contact">
        <span class="contact-text">+34 611.205.938</span>
        <span class="contact-icon">
          <svg viewBox="0 0 14 14"><rect x="3.5" y="1" width="7" height="12" rx="1.5" fill="none" stroke="var(--royal)" stroke-width="1.6"/><circle cx="7" cy="10.6" r="0.9" fill="var(--royal)"/></svg>
        </span>
      </li>
      <li class="contact">
        <span class="contact-text">www.brivomatex.example</span>
        <span class="contact-icon">
          <svg viewBox="0 0 14 14"><circle cx="7" cy="7" r="6" fill="var(--royal)"/><path d="M1,7 H13 M7,1 V13 M2.5,4 H11.5 M2.5,10 H11.5" stroke="var(--white)" stroke-width="0.8"/></svg>
        </span>
      </li>
      <li class="contact">
        <span class="contact-text">tommaso.ferlini@brivomatex.example</span>
        <span class="contact-icon">
          <svg viewBox="0 0 14 14"><path d="M1,7 L13,1.5 L9.5,12.5 L7,8.5 Z" fill="var(--royal)"/></svg>
        </span>
      </li>
    </ul>
  </section>

  <section class="card card-back">
    <div class="brand brand-back">
      <span class="brand-name">BrivoMatex</span>
      <span class="brand-dot"></span>
    </div>
    <div class="back-web">www.brivomatex.example</div>
  </section>

</body>
</html>
```